business card for a massage therapy practice named 'Meadow and Willow Massage Studio'

I really need a trendy, yet easy on the eyes business card to complement my logo. Ideally with some gold or rose gold foil work.

My uploaded file of the logo I have in horizontal but I have a vertical version as well. Another color that is used in the website is a blush pink here and there. I'd like to see some trendy tropical leaves in the design.

```html
<!DOCTYPE html>
<html lang="en">
<head>
<meta charset="utf-8">
<title>Meadow &amp; Willow Massage Studio – Business Card</title>
<link rel="stylesheet" href="https://fonts.googleapis.com/css2?family=Jost:wght@400;500;600&display=swap">
<style>
  :root {
    --backdrop: #1f1f1f;
    --paper: #ffffff;
    --sand: #9a845e;
    --seafoam: #86cfb8;
    --ink: #222222;
    --on-sand: #ffffff;
  }
  * { margin: 0; padding: 0; box-sizing: border-box; }
  html, body { width: 1200px; height: 897px; overflow: hidden; }
  body {
    background: var(--backdrop);
    font-family: "Jost", sans-serif;
    position: relative;
  }
  .card {
    position: absolute;
    left: 347px;
    width: 499px;
    height: 284px;
    overflow: hidden;
  }
  .card--front { top: 158px; background: var(--paper); }
  .card--back  { top: 465px; background: var(--sand); }

  .card__waves { position: absolute; inset: 0; width: 499px; height: 284px; }

  .brand {
    position: absolute;
    display: flex;
    align-items: center;
    gap: 10px;
  }
  .brand__dot {
    width: 26px; height: 26px;
    border-radius: 50%;
    flex: none;
  }
  .brand__name {
    font-weight: 500;
    line-height: 1.15;
    letter-spacing: 0.02em;
  }
  .card--front .brand { left: 30px; top: 34px; }
  .card--front .brand__dot { background: var(--sand); }
  .card--front .brand__name { color: var(--ink); font-size: 21px; }

  .card--back .brand {
    left: 0; right: 0; top: 88px;
    justify-content: center;
  }
  .card--back .brand__dot { background: var(--on-sand); width: 34px; height: 34px; }
  .card--back .brand__name { color: var(--on-sand); font-size: 28px; }
  .brand__line { display: block; }
  .brand__sub { display: block; font-size: 0.62em; letter-spacing: 0.2em; text-transform: uppercase; }

  .holder {
    position: absolute;
    right: 13px;
    top: 154px;
    text-align: right;
    color: var(--on-sand);
  }
  .holder__name { font-size: 17px; font-weight: 600; letter-spacing: 0.01em; line-height: 1; }
  .holder__role { font-size: 10px; font-weight: 400; margin-top: 8px; letter-spacing: 0.04em; }

  .contact {
    position: absolute;
    right: 8px;
    top: 216px;
    list-style: none;
    color: var(--on-sand);
    font-size: 9.5px;
    line-height: 14.5px;
    text-align: right;
  }
  .contact__item { display: flex; justify-content: flex-end; align-items: center; gap: 6px; }
  .contact__icon { width: 7px; height: 7px; flex: none; }

  .back__web {
    position: absolute;
    left: 0; right: 0;
    top: 237px;
    text-align: center;
    color: var(--on-sand);
    font-size: 12px;
    font-weight: 600;
    letter-spacing: 0.03em;
  }
</style>
</head>
<body>

<section class="card card--front" aria-label="Business card front">
  <svg class="card__waves" viewBox="0 0 499 284" aria-hidden="true">
    <path fill="var(--seafoam)" d="M0,188 C20,228 80,254 160,238 C260,216 340,100 430,78 C465,70 490,80 499,92 L499,284 L0,284 Z"/>
    <path fill="var(--paper)" d="M0,208 C30,244 90,259 170,245 C270,224 340,116 430,96 C465,89 490,96 499,106 L499,284 L0,284 Z"/>
    <path fill="var(--sand)" d="M0,220 C35,251 95,264 175,250 C275,231 340,126 430,106 C465,99 490,104 499,110 L499,284 L0,284 Z"/>
    <path fill="var(--paper)" d="M378,112 C420,98 478,104 499,152 L499,132 C472,104 425,98 378,112 Z"/>
  </svg>

  <div class="brand">
    <span class="brand__dot"></span>
    <p class="brand__name">
      <span class="brand__line">Meadow &amp; Willow</span>
      <span class="brand__sub">Massage Studio</span>
    </p>
  </div>

  <div class="holder">
    <p class="holder__name">DARA LINWOOD</p>
    <p class="holder__role">Vice President</p>
  </div>

  <ul class="contact">
    <li class="contact__item">+961 70 482 190
      <svg class="contact__icon" viewBox="0 0 10 10"><path fill="var(--on-sand)" d="M2,0.5 L4,2.5 L3,4 C3.8,5.5 4.6,6.3 6,7 L7.5,6 L9.5,8 L8,9.5 C4,9 1,6 0.5,2 Z"/></svg>
    </li>
    <li class="contact__item">dara@meadowwillow.com
      <svg class="contact__icon" viewBox="0 0 10 10"><rect x="0.7" y="2" width="8.6" height="6" fill="none" stroke="var(--on-sand)" stroke-width="1.2"/><path d="M0.7,2 L5,5.5 L9.3,2" fill="none" stroke="var(--on-sand)" stroke-width="1"/></svg>
    </li>
    <li class="contact__item">www.meadowwillow.com
      <svg class="contact__icon" viewBox="0 0 10 10"><circle cx="5" cy="5" r="4.2" fill="none" stroke="var(--on-sand)" stroke-width="1.1"/><path d="M0.8,5 H9.2 M5,0.8 C2.8,3 2.8,7 5,9.2 M5,0.8 C7.2,3 7.2,7 5,9.2" fill="none" stroke="var(--on-sand)" stroke-width="0.8"/></svg>
    </li>
  </ul>
</section>

<section class="card card--back" aria-label="Business card back">
  <div class="brand">
    <span class="brand__dot"></span>
    <p class="brand__name">
      <span class="brand__line">Meadow &amp; Willow</span>
      <span class="brand__sub">Massage Studio</span>
    </p>
  </div>
  <p class="back__web">www.yourwebsite.com</p>
</section>

</body>
</html>
```